Funk up our website

Our website is currently in operation and working well, see it at www.clearbriefhub.co.uk

However it needs some redesign work, to help it feel fresh, inviting and friendly.

We need graphic mockups (png hi-res) to pass to the dev team, to do the css work:

homepage - http://www.clearbriefhub.co.uk
topic page - http://www.clearbriefhub.co.uk/guidance/business
sub-topic - http://www.clearbriefhub.co.uk/guidance/business/goods-services
content - http://www.clearbriefhub.co.uk/guidance/business/goods-services/heads-of-terms
ancillary pages - contact us, heads of terms, etc

The structure of the page in terms of the placement of header, menu bar, content area and footer needs to remain, but the design of it is up for grabs.

The site is currently free to use, but in the future will have the aim of getting users to register for free, but with the option of buying documents on an individual basis, or subscription basis, or subscribing to additional legal services.

Additional information
---------------------------
Users
1. Owners and managers in small and medium businesses
2. In the UK only
3. Who find dealing with legal issues and lawyers intimidating
4. Who are searching for online help to try and avoid having to deal with a lawyer
5. Or have been referred via social media
Desired user experience
1. A welcoming, friendly site
2. That takes the complexity out of dealing with legal issues
3. That really does clear the brief
4. That is fast, efficient and clear
5. That is pleasantly different from the normal experience of interacting with a law firm
Relevant factors
1. Most visitors will first land on a content page (e.g. [link]) via a search result or banner advertisement – not the Home Page
2. Repeat visitors are more likely to go to the Home Page
3. Works with web responsive design techniques for display on smartphones and tablets
4. Implemented through CSS
Colour palette
Designer should feel able to build the palette around the following core colours
CMYK
YELLOW = 0,25,100,0
GREEN = 80,0,100,0
BLUE = 100,25,0,0

RGB
YELLOW = 255,195,15
GREEN = 15,175,75
BLUE = 0,140,210

PANTONE
YELLOW = 123c
GREEN = 361c
BLUE = 3005c

Fonts
Soho Gothic, Soho, Arial
Designer should feel able to add fonts to complement these core fonts.

Our logo needs to remain (see attached document) Our strap line, can be changed if needed.

Best
RK
Updates

Hi All

Some websites worth having a look at for how people have done things differently / added something distinctive to their website:

http://www.brevicounsel.co.uk/
https://www.tandelegal.co.uk/
http://www.quillatrix.com/

Cheers
RK

Hi All

Thanks for your designs. Just back in the office today, we will discuss and feedback / decide asap.

Best
RK

```html
<!DOCTYPE html>
<html lang="en">
<head>
<meta charset="utf-8">
<title>Clear Brief Hub — Home</title>
<link rel="stylesheet" href="https://fonts.googleapis.com/css2?family=Arimo:wght@400;700&family=Fira+Sans:wght@400&display=swap">
<style>
:root{
  --green:#1cb14b;
  --blue:#2f6db1;
  --blue-dark:#285f9c;
  --heading:#2c6aa8;
  --yellow:#f5b51b;
  --teal:#1a9fd0;
  --text:#555;
  --ink:#222;
  --band:#2a2a2a;
  --rule:#e2e2e2;
}
*{box-sizing:border-box;margin:0;padding:0}
html,body{width:1043px;height:1200px;overflow:hidden;background:#fff}
body{position:relative;font-family:"Arimo",Arial,sans-serif;color:var(--text)}
.abs{position:absolute}
a{color:inherit;text-decoration:none}

/* header */
.brand{left:160px;top:28px;display:flex;align-items:center;gap:10px;font-weight:700;font-size:26px;color:var(--ink);letter-spacing:-.5px}
.brand-mark{width:34px;height:34px;background:var(--green)}
.tagline{left:496px;top:22px;font-family:"Fira Sans",Arial,sans-serif;font-size:18px;color:var(--ink);line-height:22px}
.tagline .accent{display:block;text-align:right;padding-right:0;color:var(--teal);font-size:17px}
.tagline .fast{color:var(--yellow)}
.tagline .eff{color:var(--green)}
.btn{display:flex;align-items:center;justify-content:center;color:#fff;font-size:10px;border-radius:2px}
.btn-green{background:var(--green)}
.btn-blue{background:var(--blue)}
.register{left:728px;top:37px;width:76px;height:22px}
.login{left:810px;top:37px;width:76px;height:22px}

/* nav */
.nav{left:157px;top:90px;width:730px;height:37px;background:var(--blue);display:flex;align-items:center}
.nav a{color:#fff;font-size:10.5px;height:37px;display:flex;align-items:center;justify-content:center}
.nav .active{background:var(--green);width:89px}
.nav .item{padding:0 22px}
.search{left:702px;top:97px;width:176px;height:22px;background:#fff;border:1px solid #c9d6e6;border-radius:2px;font-size:7px;color:#777;padding:7px 10px}
.search svg{position:absolute;right:7px;top:5px}

/* hero */
.hero{left:157px;top:138px;width:730px;height:291px;background:linear-gradient(90deg,#6f7b86,#b7a08e 45%,#9aa3ad 60%,#5f6b78)}
.hero-caption{left:157px;top:362px;width:730px;height:67px;background:rgba(70,70,70,.85);color:#fff;padding:12px 17px}
.hero-caption h2{font-weight:400;font-size:18px;margin-bottom:6px}
.hero-caption p{font-size:11.5px;color:#eee}
.hero-pager{right:14px;top:25px;display:flex;gap:2px}
.hero-pager span{width:19px;height:19px;background:rgba(255,255,255,.12);display:flex;align-items:center;justify-content:center}
.hero-arrow{top:253px;width:28px;height:28px;border-radius:50%;background:rgba(255,255,255,.15)}

/* intro */
.section-title{font-weight:400;color:var(--heading)}
.intro-title{left:159px;top:455px;font-size:15.5px}
.video{left:159px;top:494px;width:298px;height:180px;border:1px solid #bbb}
.video-frame{width:100%;height:161px;background:linear-gradient(135deg,#3b2a1c,#1a140f 60%,#5a3a22)}
.video-bar{height:17px;background:linear-gradient(#f4f4f4,#d8d8d8);display:flex;align-items:center;gap:6px;padding:0 6px;font-size:7.5px;font-weight:700;color:#222}
.video-bar .track{flex:1;height:4px;background:#aaa;border-radius:2px}
.intro-text{left:482px;top:496px;width:408px;font-size:8.6px;line-height:17.2px}
.intro-btn{left:482px;top:629px;width:236px;height:33px;font-size:9px}

/* band */
.band{left:157px;top:702px;width:730px;height:83px;background:var(--band);border-right:2px solid var(--blue)}
.band-photo{left:0;top:0;width:200px;height:83px;background:linear-gradient(90deg,#d9d4cf,#8a8580 70%,var(--band))}
.band h3{left:200px;top:22px;color:#fff;font-weight:400;font-size:17.5px}
.band p{left:200px;top:50px;color:#fff;font-size:11.5px}
.band-btn{left:612px;top:28px;width:92px;height:32px;font-size:12.5px}

/* columns */
.col-title{top:808px;font-size:15.5px}
.col-photo{top:835px;width:220px;height:110px}
.col-text{top:962px;width:222px;font-size:7.8px;line-height:15.7px;color:#444}
.more{top:1065px;width:123px;height:29px;font-size:9px}

.visitor{left:670px;width:218px;height:63px;border-bottom:1px solid var(--rule);display:flex;gap:9px}
.visitor .thumb{width:60px;height:53px;border:1px solid #ddd;padding:2px;flex:none}
.visitor .thumb div{width:100%;height:100%;background:linear-gradient(#dfe6ec,#c7ccd0)}
.visitor h4{font-weight:400;font-size:10px;color:var(--heading);margin:6px 0 5px}
.visitor p{font-size:7.8px;line-height:15.5px;color:#444}

/* footer */
.footer{left:0;top:1130px;width:1043px;height:70px;background:var(--blue-dark)}
.footer-links{left:159px;top:19px;font-size:8px;color:#fff;display:flex;gap:9px}
.footer-copy{left:159px;top:40px;font-size:7.8px;color:#fff}
.social{top:22px;width:24px;height:24px;border-radius:50%;background:rgba(255,255,255,.18)}
</style>
</head>
<body>

<header>
  <div class="abs brand"><span class="brand-mark"></span>Clear Brief Hub</div>
  <div class="abs tagline">Making legal services<span class="accent"><span class="fast">fast,</span> <span class="eff">efficient</span> &amp; clear.</span></div>
  <a class="abs btn btn-green register" href="#">Register</a>
  <a class="abs btn btn-blue login" href="#">Login</a>
</header>

<nav class="abs nav">
  <a class="active" href="#">Home</a>
  <a class="item" href="#">Guide yourself</a>
  <a class="item" href="#">Draft yourself</a>
  <a class="item" href="#">Search for a lawyer</a>
  <a class="item" href="#">Get your drafts</a>
</nav>
<div class="abs search">SEARCH :
  <svg width="12" height="12" viewBox="0 0 12 12"><circle cx="5" cy="5" r="3.5" fill="none" stroke="#aaa" stroke-width="1.3"/><path d="M7.6 7.6 11 11" stroke="#aaa" stroke-width="1.6"/></svg>
</div>

<section>
  <div class="abs hero" role="img" aria-label="Photo of two business people in suits shaking hands"></div>
  <div class="abs hero-arrow" style="left:167px"></div>
  <div class="abs hero-arrow" style="left:850px"></div>
  <div class="abs hero-caption">
    <h2>Free legal support for you and your business</h2>
    <p>This site uses cookies to ensure that we give you the best experience possible. If you continue without changing...</p>
    <div class="abs hero-pager">
      <span><svg width="6" height="9"><path d="M5 1 1 4.5 5 8" fill="none" stroke="#ccc"/></svg></span>
      <span><svg width="6" height="9"><path d="M1 1 5 4.5 1 8" fill="none" stroke="#ccc"/></svg></span>
    </div>
  </div>
</section>

<section>
  <h2 class="abs section-title intro-title">Free legal support for you and your business</h2>
  <div class="abs video">
    <div class="video-frame" role="img" aria-label="Video still of law books and a wooden gavel"></div>
    <div class="video-bar">
      <svg width="6" height="7"><path d="M0 0 6 3.5 0 7z" fill="#111"/></svg>
      <span>00:00</span><span class="track"></span><span>00:00</span>
      <svg width="24" height="7"><path d="M0 2h2l2-2v7l-2-2H0z" fill="#333"/><path d="M7 5v2M9 4v3M11 3v4M13 2v5M15 1v6M17 0v7" stroke="#333"/></svg>
      <svg width="8" height="8"><path d="M0 3V0h3M5 0h3v3M8 5v3H5M3 8H0V5" fill="none" stroke="#333"/></svg>
    </div>
  </div>
  <p class="abs intro-text">This site uses cookies to ensure that we give you the best experience possible. If you continue without changing your browser settings to decline or restrict cookies, or click on Accept Cookies, you are consenting to receive all cookies from our site. For more information on the cookies we use and how to disable them see our Privacy Policy.This site uses cookies to ensure that we give you the best experience possible. If you continue without changing your browser settings to decline or restrict cookies, or click on Accept Cookies, you are consenting to receive all cookies from our site. For more information on the cookies we use and how to disable them see our Privacy Policy.</p>
  <a class="abs btn btn-blue intro-btn" href="#">Click here to register and start drafting for free</a>
</section>

<section class="abs band">
  <div class="abs band-photo" role="img" aria-label="Photo of hands typing on a laptop keyboard"></div>
  <h3 class="abs">MOST VISITORS</h3>
  <p class="abs">This site uses cookies to ensure that we give you the best experience possible.</p>
  <a class="abs btn btn-green band-btn" href="#">Click here</a>
</section>

<section>
  <h3 class="abs section-title col-title" style="left:157px">Business</h3>
  <div class="abs col-photo" style="left:157px;background:linear-gradient(135deg,#e9eef3,#c9d3dc 60%,#2f7fc6)" role="img" aria-label="Photo of a contract with a pen, calculator and glasses"></div>
  <p class="abs col-text" style="left:157px">This site uses cookies to ensure that we give you the best experience possible. If you continue without changing your browser settings to decline or restrict cookies, or click on Accept Cookies, you are consenting to receive all cookies from our site.</p>
  <a class="abs btn btn-green more" style="left:157px" href="#">Click here for more info</a>

  <h3 class="abs section-title col-title" style="left:414px">Personal</h3>
  <div class="abs col-photo" style="left:414px;background:linear-gradient(90deg,#6b5a4c,#2b2a33 45%,#7a5a3e)" role="img" aria-label="Photo of a lawyer in a gown seated before a bookcase"></div>
  <p class="abs col-text" style="left:414px">This site uses cookies to ensure that we give you the best experience possible. If you continue without changing your browser settings to decline or restrict cookies, or click on Accept Cookies, you are consenting to receive all cookies from our site.</p>
  <a class="abs btn btn-blue more" style="left:414px" href="#">Click here for more info</a>

  <h3 class="abs section-title col-title" style="left:670px">Repeat visitors</h3>
  <div class="abs visitor" style="top:846px">
    <div class="thumb"><div role="img" aria-label="Portrait photo of a smiling woman"></div></div>
    <div><h4>Marcus Elden</h4><p>This site uses cookies to ensure that we give you the best experience possible.</p></div>
  </div>
  <div class="abs visitor" style="top:921px">
    <div class="thumb"><div role="img" aria-label="Portrait photo of an older man"></div></div>
    <div><h4>Marcus Elden</h4><p>This site uses cookies to ensure that we give you the best experience possible.</p></div>
  </div>
  <div class="abs visitor" style="top:996px;border-bottom:0">
    <div class="thumb"><div role="img" aria-label="Photo of a man working at a desk"></div></div>
    <div><h4>Marcus Elden</h4><p>This site uses cookies to ensure that we give you the best experience possible.</p></div>
  </div>
  <a class="abs btn btn-blue more" style="left:671px" href="#">Click here for more info</a>
</section>

<footer class="abs footer">
  <div class="abs footer-links">
    <a href="#">Contact us</a><span>|</span><a href="#">About us</a><span>|</span><a href="#">Terms and conditions</a><span>|</span><a href="#">Privacy policy</a><span>|</span><a href="#">Terminate user account</a><span>|</span><a href="#">FAQs for users</a><span>|</span><a href="#">If you're a lawyer</a>
  </div>
  <div class="abs footer-copy">Copyrights © Lucent Legal Limited 2013. All rights reserved.</div>
  <span class="abs social" style="left:803px"></span>
  <span class="abs social" style="left:832px"></span>
  <span class="abs social" style="left:862px"></span>
</footer>

</body>
</html>
```